Business Card Design Project

Basic business card with minimal details. I just need company name, email & web address, telephone and my name.
I would like the back of the card to be grey with my logo & company name centred.

Target Market(s)

Architects
Builders
Property Developers

Industry/Entity Type

Business

Font styles to use
Sans Serif

Colors

Designer to choose colors to be used in the design.

Requirements
Must have
• Framewise Build
Marcus Helby - Director
M: 0427 593184
E: marcus@framewisebuild.com.au
W: www.framewisebuild.com.au
Should not have
• No other images or pictures

```html
<!DOCTYPE html>
<html lang="en">
<head>
<meta charset="utf-8">
<title>Framewise Build — Business Card</title>
<link href="https://fonts.googleapis.com/css2?family=Open+Sans:wght@400;600&display=swap" rel="stylesheet">
<style>
  :root {
    --backdrop: #2b2b2c;
    --card: #4d5c68;
    --card-tone: #475561;
    --accent: #b0153f;
    --ink: #ffffff;
    --ink-soft: #e6eaee;
  }
  * { box-sizing: border-box; margin: 0; padding: 0; }
  html, body {
    width: 1200px; height: 900px; overflow: hidden;
    background: var(--backdrop);
    font-family: "Open Sans", Arial, sans-serif;
  }
  .canvas {
    position: relative; width: 1200px; height: 900px;
  }
  .card {
    position: absolute; top: 300px;
    width: 520px; height: 300px;
    background: var(--card);
    box-shadow: 0 4px 10px rgba(0,0,0,0.45);
    overflow: hidden;
    color: var(--ink);
  }
  .card--back { left: 60px; }
  .card--front { left: 620px; }

  .card__texture {
    position: absolute; inset: 0;
    background: linear-gradient(120deg, var(--card) 0%, var(--card-tone) 50%, var(--card) 100%);
    opacity: 0.7;
  }

  .brand {
    position: absolute;
    display: flex; align-items: center; gap: 12px;
    font-weight: 600; color: var(--ink);
    letter-spacing: 0.06em; text-transform: uppercase;
    white-space: nowrap;
  }
  .brand__mark {
    width: 18px; height: 18px; background: var(--accent); flex: none;
  }
  .card--back .brand {
    left: 50%; top: 138px; transform: translateX(-50%);
    font-size: 24px;
  }
  .card--back .brand__mark { width: 22px; height: 22px; }
  .card--front .brand {
    left: 40px; top: 52px;
    font-size: 22px;
  }

  .contact {
    position: absolute; left: 122px; top: 158px;
  }
  .contact__name { font-size: 17px; font-weight: 600; line-height: 22px; }
  .contact__role { font-size: 13px; font-weight: 600; line-height: 20px; margin-bottom: 14px; }
  .contact__list { list-style: none; font-size: 13.5px; line-height: 20px; color: var(--ink-soft); }
  .contact__label { display: inline-block; width: 18px; }
</style>
</head>
<body>
<main class="canvas">
  <section class="card card--back">
    <div class="card__texture" role="img" aria-label="Faint tonal background decoration"></div>
    <div class="brand"><span class="brand__mark"></span>Framewise Build</div>
  </section>

  <section class="card card--front">
    <div class="card__texture" role="img" aria-label="Faint tonal background decoration"></div>
    <div class="brand"><span class="brand__mark"></span>Framewise Build</div>
    <div class="contact">
      <p class="contact__name">Marcus Helby</p>
      <p class="contact__role">Director</p>
      <ul class="contact__list">
        <li><span class="contact__label">M</span>0427 593 184</li>
        <li><span class="contact__label">E</span>marcus@framewisebuild.com.au</li>
        <li><span class="contact__label">W</span>www.framewisebuild.com.au</li>
      </ul>
    </div>
  </section>
</main>
</body>
</html>
```